Popup-Fenster Design für Öffnungszeiten
Zielgruppe
Planung und Realisierung von individuellen Kaminen.
Aufgabenstellung
Für unsere Website www.wandelhof-nordau.de benötigen wir ein Popup-Fenster für die Startseite. Da das Geschäft nicht jeden Tag und zu festen Zeit geöffnet hat, soll der Kunde direkt sehen können, wann das Geschäft das nächste Mal geöffnet hat. Das Popup-Fenster soll auffällig, jedoch nicht überladen und aufdringlich sein. Einen eigenen Entwurf (der mir nicht gefällt) habe ich hochgeladen. Vielleicht benötigt dieser nur noch einen Feinschliff!? Es muss nicht reckteckig sein, ich bin auch für runde oder ovale Formen offen. Der dort eingesetzte Text sollte als Platzhalter eingesetzt werden. Bei Fragen können Sie mir gerne eine Nachricht zukommen lassen.

```html
<!DOCTYPE html>
<html lang="de">
<head>
<meta charset="utf-8">
<title>Wandelhof – Popup Öffnungszeiten</title>
<link href="https://fonts.googleapis.com/css2?family=Oswald:wght@300;400&family=Raleway:wght@200;300&family=Playfair+Display:ital,wght@1,700&family=Source+Sans+3:wght@400&family=Libre+Franklin:wght@700&display=swap" rel="stylesheet">
<style>
  :root {
    --page-grey: #e4e4e4;
    --page-white: #ffffff;
    --sidebar: #1c1c1c;
    --panel-dark: #1b1b1b;
    --panel-black: #000000;
    --gold-light: #e2cc80;
    --gold: #c9b06a;
    --gold-dark: #8c7a4c;
    --nav-text: #9a9a9a;
    --hero-title: #8f9296;
  }
  * { box-sizing: border-box; margin: 0; padding: 0; }
  html, body { width: 960px; height: 1200px; overflow: hidden; }
  body {
    position: relative;
    background: linear-gradient(to bottom, var(--page-grey) 0, var(--page-grey) 904px, var(--page-white) 904px);
    font-family: "Source Sans 3", sans-serif;
  }

  /* Website view */
  .site { position: absolute; left: 0; top: 0; width: 960px; height: 484px; overflow: hidden; }
  .sidebar { position: absolute; left: 0; top: 0; width: 146px; height: 484px; background: var(--sidebar); }
  .sidebar-brand { position: absolute; top: 30px; left: 0; width: 146px; text-align: center; }
  .sidebar-brand .brand-square { display: block; width: 24px; height: 24px; margin: 0 auto 8px; background: var(--gold); }
  .sidebar-brand .brand-name { font-family: "Oswald", sans-serif; font-weight: 300; font-size: 8px; letter-spacing: 3px; color: var(--gold); }
  .nav { position: absolute; left: 20px; top: 125px; list-style: none; }
  .nav li { font-family: "Raleway", sans-serif; font-weight: 300; font-size: 9px; color: var(--nav-text); height: 26.2px; line-height: 14px; }
  .legal { position: absolute; left: 20px; top: 462px; font-family: "Raleway", sans-serif; font-size: 6px; color: var(--gold-dark); }
  .hero-photo {
    position: absolute; left: 146px; top: 0; width: 814px; height: 484px;
    background: linear-gradient(to bottom, #4a4135 0, #3b424c 6%, #4c5560 30%, #5a5b58 48%, #66645e 62%, #4c4a47 80%, #3e3a36 100%);
  }
  .hero-title {
    position: absolute; left: 146px; width: 814px; top: 198px; text-align: center;
    font-family: "Raleway", sans-serif; font-weight: 200; font-size: 33px; color: var(--hero-title); letter-spacing: 0;
  }
  .hero-tagline {
    position: absolute; left: 146px; width: 814px; top: 238px; text-align: center;
    font-family: "Playfair Display", serif; font-style: italic; font-weight: 700; font-size: 22px; color: #5a5a5e;
  }
  .hero-cta { position: absolute; left: 473px; top: 443px; font-family: "Raleway", sans-serif; font-size: 7px; letter-spacing: 2px; color: #2c2c2c; }
  .popup-small { position: absolute; left: 520px; top: 285px; transform: scale(0.4); transform-origin: 0 0; }
  .close-button { position: absolute; left: 860px; top: 267px; width: 32px; height: 32px; }

  /* Popup */
  .popup { position: absolute; width: 888px; height: 444px; display: flex; box-shadow: 0 0 4px rgba(0,0,0,0.25); }
  .popup-large { left: 36px; top: 574px; }
  .popup-info { position: relative; width: 542px; height: 444px; background: var(--panel-dark); text-align: center; }
  .popup-side { position: relative; width: 346px; height: 444px; background: var(--panel-black); overflow: hidden; }
  .popup-title {
    position: absolute; left: 0; width: 542px; top: 16px;
    font-family: "Oswald", sans-serif; font-weight: 300; font-size: 68px; letter-spacing: 5px; line-height: 80px;
    background: linear-gradient(to right, var(--gold-light), var(--gold) 45%, var(--gold-dark));
    -webkit-background-clip: text; background-clip: text; color: transparent;
  }
  .popup-intro { position: absolute; left: 0; width: 542px; top: 142px; font-size: 22px; color: var(--gold); }
  .popup-dates {
    position: absolute; left: 36px; top: 199px; width: 470px; height: 93px;
    border: 4px solid var(--gold); background: #000;
    font-family: "Libre Franklin", sans-serif; font-weight: 700; font-size: 25px; line-height: 36px; color: var(--gold-light);
    padding-top: 8px;
  }
  .popup-links { position: absolute; left: 0; width: 542px; top: 326px; list-style: none; font-size: 22px; line-height: 37px; color: var(--gold); }
  .popup-brand { position: absolute; left: 0; width: 346px; top: 62px; text-align: center; }
  .popup-brand .brand-square { display: block; width: 56px; height: 56px; margin: 0 auto 20px; background: var(--gold); }
  .popup-brand .brand-name { font-family: "Oswald", sans-serif; font-weight: 300; font-size: 22px; letter-spacing: 7px; color: var(--gold); }
  .fireplace-art {
    position: absolute; left: 52px; top: 215px; width: 243px; height: 229px;
    background: linear-gradient(to bottom, #3a3a3a 0, #5a5a5a 40%, #8a7a44 70%, #a89550 100%);
  }
</style>
</head>
<body>

<section class="site">
  <div class="hero-photo" role="img" aria-label="Raum mit Panoramafenster, hängendem Kamin und Berglandschaft"></div>
  <aside class="sidebar">
    <div class="sidebar-brand"><span class="brand-square"></span><span class="brand-name">WANDELHOF</span></div>
    <ul class="nav">
      <li>ÜBER UNS</li>
      <li>KAMINÖFEN</li>
      <li>HOLZKAMINE</li>
      <li>GASKAMINE</li>
      <li>AUSSTELLUNG</li>
      <li>KONTAKT</li>
    </ul>
    <div class="legal">Impressum | Datenschutz</div>
  </aside>
  <h1 class="hero-title">WILLKOMMEN IM WANDELHOF</h1>
  <p class="hero-tagline">KAMINE FÜRS LEBEN</p>
  <p class="hero-cta">Jetzt Beratung</p>

  <div class="popup popup-small">
    <div class="popup-info">
      <h2 class="popup-title">ÖFFNUNGSZEITEN</h2>
      <p class="popup-intro">Wir habe für Sie geöffnet</p>
      <div class="popup-dates">
        <p>Fr 17.01 &nbsp;·&nbsp; 14:00 - 17:00 Uhr</p>
        <p>Sa 18.01 &nbsp;·&nbsp; 10:00 - 13:00 Uhr</p>
      </div>
      <ul class="popup-links">
        <li>Weitere Termine ansehen</li>
        <li>Individuellen Termin vereinbaren</li>
      </ul>
    </div>
    <div class="popup-side">
      <div class="popup-brand"><span class="brand-square"></span><span class="brand-name">WANDELHOF</span></div>
      <div class="fireplace-art" role="img" aria-label="Illustration eines Kamins mit goldener Flamme"></div>
    </div>
  </div>

  <svg class="close-button" viewBox="0 0 32 32" aria-label="Schließen">
    <circle cx="16" cy="16" r="15" fill="#d8d8d8" fill-opacity="0.85"/>
    <path d="M10 10 L22 22 M22 10 L10 22" stroke="#ffffff" stroke-width="2.5" stroke-linecap="round"/>
  </svg>
</section>

<div class="popup popup-large">
  <div class="popup-info">
    <h2 class="popup-title">ÖFFNUNGSZEITEN</h2>
    <p class="popup-intro">Wir habe für Sie geöffnet</p>
    <div class="popup-dates">
      <p>Fr 17.01 &nbsp;·&nbsp; 14:00 - 17:00 Uhr</p>
      <p>Sa 18.01 &nbsp;·&nbsp; 10:00 - 13:00 Uhr</p>
    </div>
    <ul class="popup-links">
      <li>Weitere Termine ansehen</li>
      <li>Individuellen Termin vereinbaren</li>
    </ul>
  </div>
  <div class="popup-side">
    <div class="popup-brand"><span class="brand-square"></span><span class="brand-name">WANDELHOF</span></div>
    <div class="fireplace-art" role="img" aria-label="Illustration eines Kamins mit goldener Flamme"></div>
  </div>
</div>

</body>
</html>
```